Business Card Design Project 4 Construction Business

I am after a creative, but sleek and simple/ clean business card design. This design will form the basis of future items and might include a logo or simply a creative way to lay out the text of my company name 'kestrel ventures'
I like the simplicity of black and white however I would also be happy to see a splash of colour introduced somehow to give the text some interest and make it stand out.
I would like a double sided card.
I am young (ish!) and professional, offering construction and project management services, what I don't want is the traditional builders type card featuring a cheesy hammer/ saw image etc.
As the company name, kestrel ventures, suggests, we focus on working closely and collaboratively together, in synergy with all stakeholders involved in the projects that we undertake
Construction

```html
<!DOCTYPE html>
<html lang="en">
<head>
<meta charset="utf-8">
<title>Kestrel Ventures – Business Card</title>
<link href="https://fonts.googleapis.com/css2?family=Open+Sans:wght@300;400&display=swap" rel="stylesheet">
<style>
  :root {
    --backdrop: #d9dadb;
    --card: #f7f8f8;
    --brand-blue: #1f86c8;
    --band-top: #2ea3dc;
    --band-bottom: #1786c6;
    --text-grey: #8c8f92;
    --muted-grey: #a9acaf;
    --soft-blue: #a9c7e6;
    --white: #ffffff;
  }
  * { box-sizing: border-box; margin: 0; padding: 0; }
  html, body {
    width: 1200px;
    height: 901px;
    overflow: hidden;
    background: var(--backdrop);
    font-family: "Open Sans", Arial, sans-serif;
  }
  .card {
    position: absolute;
    left: 320px;
    width: 560px;
    height: 342px;
    background: var(--card);
    overflow: hidden;
    box-shadow: 0 2px 6px rgba(0,0,0,0.12);
  }
  .card--front { top: 80px; }
  .card--back  { top: 480px; }

  /* Front */
  .wordmark {
    font-weight: 300;
    color: var(--brand-blue);
    text-transform: uppercase;
    line-height: 1;
  }
  .card--front .wordmark {
    position: absolute;
    left: 44px;
    top: 112px;
  }
  .wordmark__line1 { display: block; font-size: 50px; letter-spacing: 1px; }
  .wordmark__line2 { display: block; font-size: 33px; letter-spacing: 9px; margin-top: 6px; }
  .brand-dot {
    position: absolute;
    left: 372px;
    top: 86px;
    width: 168px;
    height: 168px;
    border-radius: 50%;
    background: var(--brand-blue);
  }

  /* Back */
  .band {
    position: absolute;
    left: 0;
    top: 18px;
    width: 100%;
    height: 92px;
    background: linear-gradient(180deg, var(--band-top), var(--band-bottom));
    display: flex;
    justify-content: center;
    align-items: center;
  }
  .band .wordmark { color: var(--white); text-align: center; }
  .band .wordmark__line1 { font-size: 34px; }
  .band .wordmark__line2 { font-size: 22px; letter-spacing: 7px; margin-top: 2px; }

  .person {
    position: absolute;
    left: 30px;
    top: 118px;
  }
  .person__name {
    font-size: 36px;
    font-weight: 300;
    color: var(--text-grey);
    line-height: 1.1;
  }
  .person__role {
    font-size: 17px;
    font-weight: 300;
    color: var(--brand-blue);
  }
  .contact-list {
    position: absolute;
    left: 30px;
    top: 200px;
    list-style: none;
    font-size: 12px;
    color: var(--brand-blue);
  }
  .contact-list li {
    display: flex;
    align-items: center;
    gap: 10px;
    height: 24px;
  }
  .contact-list svg { width: 12px; height: 12px; fill: var(--muted-grey); }
  .contact-list .address {
    color: var(--muted-grey);
    font-size: 14px;
    margin-top: 4px;
  }
  .decor-circle {
    position: absolute;
    right: 40px;
    bottom: -40px;
    width: 240px;
    height: 240px;
    border-radius: 50%;
    background: var(--soft-blue);
    opacity: 0.8;
  }
</style>
</head>
<body>

<section class="card card--front" aria-label="Card front">
  <h1 class="wordmark">
    <span class="wordmark__line1">Kestrel</span>
    <span class="wordmark__line2">Ventures</span>
  </h1>
  <div class="brand-dot"></div>
</section>

<section class="card card--back" aria-label="Card back">
  <div class="band">
    <p class="wordmark">
      <span class="wordmark__line1">Kestrel</span>
      <span class="wordmark__line2">Ventures</span>
    </p>
  </div>

  <div class="person">
    <p class="person__name">Tom Ardley</p>
    <p class="person__role">Director</p>
  </div>

  <ul class="contact-list">
    <li>
      <svg viewBox="0 0 24 24" aria-hidden="true"><path d="M6.6 10.8a15.1 15.1 0 0 0 6.6 6.6l2.2-2.2a1 1 0 0 1 1-.25 11.4 11.4 0 0 0 3.6.57 1 1 0 0 1 1 1V20a1 1 0 0 1-1 1A17 17 0 0 1 3 4a1 1 0 0 1 1-1h3.5a1 1 0 0 1 1 1c0 1.25.2 2.45.57 3.57a1 1 0 0 1-.25 1z"/></svg>
      0400 118 200
    </li>
    <li>
      <svg viewBox="0 0 24 24" aria-hidden="true"><path d="M2 5h20v14H2z M2 5l10 7 10-7" /></svg>
      tom@kestrelventures.com.au
    </li>
    <li>
      <svg viewBox="0 0 24 24" aria-hidden="true"><circle cx="12" cy="12" r="10"/></svg>
      www.kestrelventures.com.au
    </li>
    <li class="address">12 Harbour St &nbsp;–&nbsp; Marsden, NSW 2100</li>
  </ul>

  <div class="decor-circle"></div>
</section>

</body>
</html>
```